Building technology company seek stationery design and folder design

Letterhead, and a folder design
ideally, I would have two letter head design, one is for one-page bussiness letter. the other one I can use for longer document such report, or analysis regular report page
you can find company logo and overall style at our website:
www.plinthcove.example

we are in building technology business, using internet of things technology to improve building energy efficiency to make building greener.

Industry/Entity Type

It Company

Requirements
Must have
• company logo
Nice to have
• techy look abstract graphics, etc.
Should not have
• no comment

```html
<!DOCTYPE html>
<html lang="en">
<head>
<meta charset="utf-8">
<title>Plinth Cove Letterheads</title>
<link href="https://fonts.googleapis.com/css2?family=Montserrat:wght@600;700&family=Open+Sans:wght@400;600&family=Great+Vibes&display=swap" rel="stylesheet">
<style>
  :root {
    --green: #a2cd3a;
    --taupe: #84826f;
    --ink: #3c3c3c;
    --muted: #6f6f6f;
    --paper: #ffffff;
    --backdrop: #e8e8e8;
  }
  * { margin: 0; padding: 0; box-sizing: border-box; }
  html, body { width: 1200px; height: 1200px; overflow: hidden; }
  body {
    background: var(--backdrop);
    font-family: "Open Sans", Arial, sans-serif;
    color: var(--ink);
    position: relative;
  }
  .sheet {
    position: absolute;
    top: 220px;
    width: 540px;
    height: 760px;
    background: var(--paper);
    overflow: hidden;
  }
  .sheet--report { left: 40px; }
  .sheet--letter { left: 620px; }

  .brand-name {
    font-family: "Montserrat", Arial, sans-serif;
    font-weight: 700;
    color: var(--green);
    letter-spacing: 1.5px;
    display: flex;
    align-items: center;
    gap: 8px;
    white-space: nowrap;
  }
  .brand-name .brand-square {
    width: 14px; height: 14px; background: var(--green);
  }

  /* report sheet */
  .title-rule {
    position: absolute; top: 40px; left: 28px; right: 210px;
    display: flex; align-items: center; gap: 10px;
  }
  .title-rule__label {
    font-family: "Montserrat", Arial, sans-serif;
    font-weight: 700; font-size: 10px; letter-spacing: 1.6px;
    color: var(--taupe); white-space: nowrap;
  }
  .title-rule__line { flex: 1; height: 2px; background: var(--green); }
  .sheet--report .brand-name {
    position: absolute; top: 33px; right: 28px; font-size: 16px;
  }
  .report-footer {
    position: absolute; left: 28px; right: 28px; bottom: 30px;
    padding-top: 10px; border-top: 1px solid var(--green);
    font-size: 9.5px; font-weight: 600; color: var(--ink);
    display: flex; align-items: center; gap: 6px;
  }
  .report-footer .dot {
    width: 8px; height: 8px; border-radius: 50%; background: var(--taupe);
  }

  /* letter sheet */
  .sheet--letter .brand-name {
    position: absolute; top: 58px; left: 30px; font-size: 20px;
  }
  .letter-contact {
    position: absolute; top: 42px; right: 34px;
    font-size: 10px; color: var(--muted);
  }
  .letter-contact__company {
    font-family: "Montserrat", Arial, sans-serif;
    font-weight: 700; font-size: 8.5px; letter-spacing: 1.6px;
    color: var(--green); margin-bottom: 5px;
  }
  .letter-contact__row {
    display: flex; align-items: center; gap: 6px; line-height: 14px;
  }
  .letter-contact svg { width: 9px; height: 9px; fill: var(--green); }

  .letter-body {
    position: absolute; top: 244px; left: 60px; width: 430px;
    font-size: 9.3px; line-height: 22px; color: var(--ink);
  }
  .letter-body p + p { margin-top: 22px; }
  .recipient { margin-bottom: 22px; }
  .sign-off { margin-top: 30px; padding-left: 18px; }
  .signature {
    font-family: "Great Vibes", cursive;
    font-size: 28px; color: var(--muted); line-height: 32px;
  }

  .letter-footer {
    position: absolute; left: 0; bottom: 0; width: 540px; height: 86px;
  }
  .letter-footer__accent {
    position: absolute; top: 0; left: 0; width: 540px; height: 6px;
    background: var(--green);
  }
  .letter-footer__band {
    position: absolute; top: 12px; left: 0; right: 0; bottom: 0;
    background: var(--taupe);
  }
  .letter-footer__url {
    position: absolute; right: 26px; bottom: 24px;
    color: #fff; font-size: 15px;
  }
</style>
</head>
<body>

  <section class="sheet sheet--report">
    <div class="title-rule">
      <span class="title-rule__label">PLINTH COVE PVT. LTD.</span>
      <span class="title-rule__line"></span>
    </div>
    <div class="brand-name"><span class="brand-square"></span>PLINTH COVE</div>
    <footer class="report-footer">
      <span class="dot"></span>
      T: (555) 014-2273 | E: info@plinthcove.example | W: www.plinthcove.example
    </footer>
  </section>

  <section class="sheet sheet--letter">
    <div class="brand-name"><span class="brand-square"></span>PLINTH COVE</div>

    <div class="letter-contact">
      <div class="letter-contact__company">PLINTH COVE PVT. LTD.</div>
      <div class="letter-contact__row">
        <svg viewBox="0 0 10 10"><path d="M1 3 Q5 0 9 3 L8 4.5 L6.5 3.8 L6.5 3 Q5 2.5 3.5 3 L3.5 3.8 L2 4.5 Z M2 5 H8 V9 H2 Z"/></svg>
        (555) 014-2273
      </div>
      <div class="letter-contact__row">
        <svg viewBox="0 0 10 10"><path d="M0 2 H10 V8.5 H0 Z"/><path d="M0.5 2.5 L5 6 L9.5 2.5" stroke="#fff" stroke-width="1" fill="none"/></svg>
        info@plinthcove.example
      </div>
    </div>

    <article class="letter-body">
      <div class="recipient">To<br>The,<br>Director</div>
      <p>Lorem ipsum dolor sit amet, consectetur adipiscing elit. Sed at ante. Mauris eleifend, quam a vulptate dictum, massa quam dapibus leo, eget vulputate orci purus ut lorem. In fringilla mi in ligula. Pellen tesque aliquam quam vel dolor. Nunc adipiscing. Sed quamodio, tempus ac, aliquam molestie varius ac, tellus. Vestibulum ut nulla aliquam risus rutrum interdum. Pellentesque lorem.</p>
      <p>Curabitur sit amet &nbsp;erat quis risus feugiat viverra. Pellentesque augue justo,sagittis et, lacinia at, venenatis non, arcu. &nbsp;Nunc nec libero. In cursus dictum risus. Etiam tristique nisl a nulla. Ut a orci. Curabitur dolonunc,egestas at, accumsan at, malesuada nec, magna. Nulla facilisi. Nunc volutpat. Vestibulum ante ipsum primis in faucibus orci luctus et ultrices posuere cubilia Curae; Ut sit amet orci vel mauris blandit vehicula. Nullam quis enim. Integer dignissim viverra velit. Curabitur in odio</p>
      <div class="sign-off">
        Thanking you,
        <div class="signature">John Doe</div>
      </div>
    </article>

    <footer class="letter-footer">
      <div class="letter-footer__accent"></div>
      <div class="letter-footer__band"></div>
      <span class="letter-footer__url">www.plinthcove.example</span>
    </footer>
  </section>

</body>
</html>
```